Market online tutoring + Back to School + give Support for students school work K to 12 Grade

To promote my tutoring business online need to create a two sided flyer. Need to get the attention of parents and educators who looking for help to support the digital learning of their students due to COVID-19 lock down. I need to project and differentiate that we offer support for online school with individualized learning . We tutor Elementary to High school students on all subjects you may take a look at my website qnacademyga.com for additional info and also I can provide
Updates

Hi All Due to Covid, we were unable to work on this project on time as originally planned. We were given an extension until March 15 and we will complete it by then. Sorry for any inconvenience and Thank you for your support. -QN Academy

Target Market(s)

Parents and students

Industry/Entity Type

Education

Requirements
Must have
• For online less fine print on the first page. The phone number and support text message. Back to School , Support Online learning KEV/NUR test prep should have some focus
Nice to have
• Discuss the platform We created a platform with live instructor interaction, virtual classroom, instructional videos, assessments, and practice to support every individual student’s need. We are confident in our ability to provide the most effective distance learning experience.
Should not have
• too much clunky and packed with content. Should be easy to read with color

```html
<!DOCTYPE html>
<html lang="en">
<head>
<meta charset="utf-8">
<title>QN Academy – Back to School Flyer</title>
<link href="https://fonts.googleapis.com/css2?family=Fredoka:wght@500;600&family=Open+Sans:wght@400;600;700&family=Roboto+Slab:wght@700&display=swap" rel="stylesheet">
<style>
  :root{
    --stage:#2c2c2c;
    --navy:#12384f;
    --navy-deep:#0f2f45;
    --red:#b5121b;
    --gold:#e2b31c;
    --green:#1aa57a;
    --olive:#6f7431;
    --olive-light:#8d8f3e;
    --white:#ffffff;
    --ink:#1b1b1b;
    --heading:"Fredoka", sans-serif;
    --body:"Open Sans", sans-serif;
    --display:"Roboto Slab", serif;
  }
  *{box-sizing:border-box;margin:0;padding:0}
  html,body{width:1200px;height:900px;overflow:hidden;background:var(--stage)}
  .canvas{position:relative;width:1200px;height:900px}
  .page{position:absolute;top:120px;width:512px;height:660px;background:var(--white);overflow:hidden;box-shadow:0 6px 18px rgba(0,0,0,.45)}
  .page--front{left:50px}
  .page--back{left:638px}
  .abs{position:absolute}
  svg.abs{display:block}

  /* FRONT */
  .hero-photo{left:0;top:0;width:512px;height:440px;background:linear-gradient(160deg,var(--olive-light),var(--olive) 60%,#5a6030)}
  .headline-frame{left:40px;top:45px;width:188px;height:215px;border:3px solid var(--navy)}
  .grad-cap{left:118px;top:-2px}
  .headline{left:12px;top:38px;font-family:var(--display);font-weight:700;font-size:31px;line-height:37px;color:#eef0e4;letter-spacing:1px}
  .headline-rule{left:10px;top:156px;width:162px;height:2px;background:#e8ead8}
  .headline-sub{left:10px;top:165px;font-family:var(--body);font-weight:600;font-size:12.5px;color:var(--white)}
  .brand{left:278px;top:50px;display:flex;align-items:center;gap:10px}
  .brand-mark{width:26px;height:26px;background:var(--red)}
  .brand-name{font-family:var(--heading);font-weight:600;font-size:24px;color:var(--navy)}
  .photo-circle{border-radius:50%;border:4px solid var(--navy)}
  .circle-reading{left:20px;top:265px;width:150px;height:150px;background:radial-gradient(circle at 45% 40%,#e9c98b,#caa15c 55%,#8a6a3a)}
  .circle-teacher{left:182px;top:265px;width:150px;height:150px;background:radial-gradient(circle at 40% 45%,#f4f2ec,#f2a81d 60%,#e89a10)}
  .circle-class{left:339px;top:257px;width:156px;height:156px;background:radial-gradient(circle at 50% 55%,#c7a27d,#5c6b5f 60%,#2f3b37)}
  .box-heading{font-family:var(--heading);font-weight:600;color:var(--navy);border:3px solid var(--navy);display:flex;align-items:center;justify-content:center}
  .about-heading{left:20px;top:428px;width:146px;height:37px;font-size:23px}
  .body-text{font-family:var(--body);font-size:9.6px;line-height:12.4px;color:var(--ink)}
  .body-text p+p{margin-top:11px}
  .about-text{left:32px;top:476px;width:252px;font-size:9.2px;line-height:11.6px}
  .about-text p+p{margin-top:10px}
  .test-badge{left:315px;top:437px;width:152px;display:flex;height:24px}
  .test-badge span{flex:1;display:flex;align-items:center;justify-content:center;font-family:var(--heading);font-weight:600;font-size:18px;color:var(--white)}
  .test-badge .kev{background:var(--green)}
  .test-badge .nur{background:var(--gold)}
  .test-caption{left:315px;top:464px;width:152px;text-align:center;font-family:var(--body);font-weight:700;font-size:7.6px;color:var(--navy)}
  .contact-box{left:302px;top:490px;width:178px;height:123px;border:2px solid var(--red);padding:8px 12px}
  .contact-heading{font-family:var(--heading);font-weight:600;font-size:17px;color:var(--red);margin-bottom:10px}
  .contact-box .body-text{font-size:8px;line-height:10px}
  .contact-box .body-text p+p{margin-top:12px}
  .stripe{top:623px;height:13px}
  .stripe-front-red{left:0;width:296px;background:var(--red)}
  .stripe-front-navy{left:296px;width:216px;background:var(--navy)}

  /* BACK */
  .back-top{left:0;top:0;width:512px;height:400px;background:linear-gradient(180deg,var(--navy-deep),var(--navy))}
  .academy-heading{left:25px;top:35px;width:198px;height:37px;font-size:22px;color:var(--gold);border-color:var(--gold)}
  .back-text{left:25px;top:86px;width:468px;color:var(--white);font-size:9.7px;line-height:12px}
  .back-text .narrow{width:212px}
  .circle-boy{left:233px;top:245px;width:132px;height:132px;border:4px solid var(--gold);border-radius:50%;background:radial-gradient(circle at 50% 45%,#e8c9a6,#8a6a4a 55%,#4c3a2c)}
  .circle-mentor{left:325px;top:200px;width:160px;height:160px;border:4px solid var(--gold);border-radius:50%;background:radial-gradient(circle at 45% 50%,#f0d6c2,#c98d6c 55%,#6a3e30)}
  .section-title{left:0;top:393px;width:512px;text-align:center;font-family:var(--heading);font-weight:600;font-size:18.5px;color:var(--ink)}
  .feature{top:435px;width:144px;height:176px;border:3px solid;padding:6px 8px;text-align:center}
  .feature h3{font-family:var(--body);font-weight:700;font-size:11px;line-height:13px;min-height:34px}
  .feature .body-text{font-size:9.5px;line-height:12px}
  .feature--red{left:35px;border-color:var(--red)}
  .feature--red h3{color:var(--red)}
  .feature--gold{left:188px;border-color:var(--gold)}
  .feature--gold h3{color:var(--gold)}
  .feature--navy{left:342px;border-color:var(--navy)}
  .feature--navy h3{color:var(--navy)}
  .stripe-back{top:630px;height:17px;width:171px}
  .stripe-back-red{left:0;background:var(--red)}
  .stripe-back-gold{left:171px;background:var(--gold)}
  .stripe-back-navy{left:342px;width:170px;background:var(--navy)}
</style>
</head>
<body>
<main class="canvas">

  <!-- FRONT SIDE -->
  <section class="page page--front">
    <div class="abs hero-photo" role="img" aria-label="Photo of cheering schoolchildren raising their arms in front of a chalkboard, tinted olive"></div>

    <div class="abs headline-frame">
      <svg class="abs grad-cap" width="56" height="44" viewBox="0 0 56 44" aria-hidden="true">
        <polygon points="28,2 54,14 28,26 2,14" fill="#fff"/>
        <path d="M14,19 V30 Q28,38 42,30 V19 L28,26 Z" fill="#fff"/>
        <line x1="48" y1="16" x2="48" y2="32" stroke="#fff" stroke-width="2"/>
        <rect x="46" y="31" width="4" height="8" fill="#fff"/>
      </svg>
      <h1 class="abs headline">BACK<br>TO<br>SCHOOL</h1>
      <div class="abs headline-rule"></div>
      <p class="abs headline-sub">Support Online Learning</p>
    </div>

    <div class="abs brand">
      <span class="brand-mark" aria-hidden="true"></span>
      <span class="brand-name">QN Academy</span>
    </div>

    <svg class="abs" style="left:0;top:300px" width="512" height="160" viewBox="0 0 512 160" aria-hidden="true">
      <path d="M0,50 Q256,140 512,40 L512,160 L0,160 Z" fill="var(--navy)"/>
      <path d="M0,150 Q280,50 512,88 L512,160 L0,160 Z" fill="#fff"/>
    </svg>

    <div class="abs photo-circle circle-reading" role="img" aria-label="Photo of a young girl with glasses reading a book"></div>
    <div class="abs photo-circle circle-teacher" role="img" aria-label="Photo of a teacher holding a 'School is back' speech bubble on an orange background"></div>
    <div class="abs photo-circle circle-class" role="img" aria-label="Photo of happy kids giving thumbs up in a classroom"></div>

    <h2 class="abs box-heading about-heading">About Us</h2>
    <div class="abs body-text about-text">
      <p>QN Academy in Brookfield, Georgia is a private tutoring center which provides group coaching in Math, Reading, KEV Preparation, and Computer Programming for kids.</p>
      <p>We also provide effective coaching for standardized tests like KEV, MBST, NUR, etc. We step away from the regular coaching method and implement effective problem solving techniques and critical thinking skills to help our children achieve stronger academic results.</p>
    </div>

    <div class="abs test-badge"><span class="kev">KEVs</span><span class="nur">NURs</span></div>
    <p class="abs test-caption">EFFECTIVE TEST PREPARATION</p>

    <div class="abs contact-box">
      <h2 class="contact-heading">Contact Us</h2>
      <div class="body-text">
        <p>1450 Maple Crest Road<br>Suite #210<br>Brookfield, GA 30099</p>
        <p>customerservice@qnacademyga.com</p>
        <p>404-555-0187</p>
      </div>
    </div>

    <div class="abs stripe stripe-front-red"></div>
    <div class="abs stripe stripe-front-navy"></div>
  </section>

  <!-- BACK SIDE -->
  <section class="page page--back">
    <div class="abs back-top"></div>
    <svg class="abs" style="left:0;top:300px" width="512" height="110" viewBox="0 0 512 110" aria-hidden="true">
      <path d="M0,55 Q260,0 512,30 L512,110 L0,110 Z" fill="var(--gold)"/>
      <path d="M0,80 Q270,25 512,60 L512,110 L0,110 Z" fill="#fff"/>
    </svg>

    <h2 class="abs box-heading academy-heading">Our Academy</h2>
    <div class="abs body-text back-text">
      <p>Our Georgia Standard Education (GSE) Subjects Tutoring Programs are designed to reinforce and enhance the material that our children are learning in school only a few hours before. By focusing on a topic with our skilled teachers after school, students are guaranteed to have a strong foundation and understanding of their topics before moving on to learning more advanced skills.</p>
      <p>With our online learning course we have created a platform with live instructor interaction, virtual classroom, instructional videos, assessments, and practice to support every individual student's need. We are confident in our ability to provide the most effective distance learning experience.</p>
      <p class="narrow">QN Academy strives to improve your children's academic achievements and analytical problem solving skills. We believe that stretching a child's mind through critical thinking skills, accelerated academic programs, and exposure to computer programming and robotics at an early age will help them rise to their true potential.</p>
    </div>

    <div class="abs circle-boy" role="img" aria-label="Photo of a young boy with glasses studying at a desk"></div>
    <div class="abs circle-mentor" role="img" aria-label="Photo of a tutor helping a girl with her schoolwork"></div>

    <h2 class="abs section-title">A Place to Enrich Students' Potentials</h2>

    <article class="abs feature feature--red">
      <h3>TEST PREPARATION</h3>
      <p class="body-text">We provide specialized and effective test preparation courses in KEV. "Practice Makes Perfect". We get students into a routine of consistent practice of various concepts required for success on the KEV test.</p>
    </article>
    <article class="abs feature feature--gold">
      <h3>CRITICAL THINKING</h3>
      <p class="body-text">We provide excellent critical and analytical thinking practice. Our program also helps students develop valuable tools to properly prepare for standardized tests like LSAP, MBST, etc.</p>
    </article>
    <article class="abs feature feature--navy">
      <h3>ADVANCED ACADEMIC COACHING</h3>
      <p class="body-text">We offer advanced coaching in all academic subjects for grade 1 to grade 12. Our Mathematics and Language Arts courses follow common core standards.</p>
    </article>

    <div class="abs stripe-back stripe-back-red"></div>
    <div class="abs stripe-back stripe-back-gold"></div>
    <div class="abs stripe-back stripe-back-navy"></div>
  </section>

</main>
</body>
</html>
```